Circlepage Ad for “5 Day Personal Image Sprint”

I would like a Circlepage ad graphic for this offer:
https://www.morvitaplan.com/5-day-personal-branding-challenge
Please include my photo- I have attached images to use (remove the background)
The big selling points are the three focus points during the challenge (Circlepage Page, Careerlink profile and the web site) and the cost is only $5.40
I will choose the winner who submits one ad, and then the winner will be asked to provide two variations of the ad graphic so I can test all three graphics.
Thank you, I’m looking forward to seeing your ideas and designs!

```html
<!DOCTYPE html>
<html lang="en">
<head>
<meta charset="utf-8">
<title>5 Day Personal Image Sprint – Ad</title>
<link rel="stylesheet" href="https://fonts.googleapis.com/css2?family=Oswald:wght@500;600;700&family=Lato:wght@400;700&family=Kaushan+Script&display=swap">
<style>
  :root {
    --paper: #ececec;
    --navy: #2c3b8c;
    --navy-deep: #2a3987;
    --sky: #29b8f0;
    --ink: #1d1d1d;
    --white: #ffffff;
  }
  html, body {
    margin: 0;
    padding: 0;
    width: 1200px;
    height: 1200px;
    overflow: hidden;
    background: var(--paper);
  }
  .ad {
    position: relative;
    width: 1200px;
    height: 1200px;
    background: linear-gradient(135deg, #f0f0f0 0%, #e6e6e6 100%);
    font-family: "Lato", Arial, sans-serif;
    color: var(--ink);
    overflow: hidden;
  }
  .offer-band {
    position: absolute;
    left: 0; top: 509px;
    width: 1200px; height: 263px;
    background: var(--navy);
  }
  .corner-block {
    position: absolute;
    left: 750px; top: 803px;
    width: 450px; height: 397px;
    background: var(--navy-deep);
  }
  .portrait {
    position: absolute;
    left: 700px; top: 200px;
    width: 480px; height: 990px;
    border-radius: 200px 200px 24px 24px;
    background: linear-gradient(180deg, #3a3f4c 0%, #262a36 45%, #1f2640 80%, #2a4fb8 100%);
    opacity: 0.92;
  }
  .brand {
    position: absolute;
    left: 56px; top: 72px;
    display: flex;
    align-items: center;
    gap: 18px;
  }
  .brand-square {
    width: 52px; height: 52px;
    background: var(--navy);
  }
  .brand-name {
    font-family: "Lato", Arial, sans-serif;
    font-weight: 700;
    font-size: 36px;
    letter-spacing: 0.5px;
    color: var(--navy);
    text-transform: uppercase;
  }
  .headline {
    position: absolute;
    left: 30px; top: 240px;
    width: 650px;
    margin: 0;
    text-align: center;
    font-family: "Oswald", Impact, sans-serif;
    font-weight: 700;
    font-size: 86px;
    line-height: 100px;
    color: var(--navy);
    text-transform: uppercase;
  }
  .tag {
    position: absolute;
    left: 149px;
    width: 402px;
    background: var(--sky);
    color: var(--white);
    text-align: center;
  }
  .tag-sprint {
    top: 463px; height: 90px;
    font-family: "Kaushan Script", cursive;
    font-size: 62px;
    line-height: 90px;
  }
  .tag-grow {
    top: 724px; height: 88px;
    font-family: "Oswald", Impact, sans-serif;
    font-weight: 500;
    font-size: 42px;
    line-height: 88px;
  }
  .offer-copy {
    position: absolute;
    left: 40px; top: 570px;
    width: 570px;
    margin: 0;
    text-align: center;
    color: var(--white);
    font-size: 24px;
    line-height: 38px;
  }
  .channels {
    position: absolute;
    left: 30px; top: 830px;
    width: 650px;
    display: grid;
    grid-template-columns: 200px 215px 200px;
    column-gap: 16px;
    text-align: center;
  }
  .channel-title {
    margin: 0 0 8px;
    font-family: "Oswald", Impact, sans-serif;
    font-weight: 600;
    font-size: 27px;
    color: var(--ink);
    text-transform: uppercase;
  }
  .channel-text {
    margin: 0;
    font-size: 20px;
    line-height: 26px;
  }
  .channel-text.small {
    font-size: 16.5px;
    line-height: 22px;
  }
  .cta {
    position: absolute;
    left: 176px; top: 1098px;
    width: 348px; height: 50px;
    background: var(--sky);
    color: var(--white);
    font-family: "Oswald", Impact, sans-serif;
    font-weight: 500;
    font-size: 27px;
    line-height: 50px;
    letter-spacing: 1px;
    text-align: center;
  }
</style>
</head>
<body>
  <main class="ad">
    <div class="offer-band"></div>
    <div class="corner-block"></div>
    <div class="portrait" role="img" aria-label="Cut-out photo of the coach seated, wearing a dark t-shirt, jeans and blue sneakers"></div>

    <div class="brand">
      <span class="brand-square"></span>
      <span class="brand-name">Halvorsen Group</span>
    </div>

    <h1 class="headline">5 Day Personal<br>Image</h1>
    <div class="tag tag-sprint">Sprint</div>

    <p class="offer-copy">For ONLY $5.40 (the exact price of my favorite Brewline drink) you get my quick action, take-me-by-the-hands guide to get your personal online presence set up.</p>

    <div class="tag tag-grow">Ready to Grow:</div>

    <section class="channels">
      <div class="channel">
        <h2 class="channel-title">Circlepage</h2>
        <p class="channel-text">That you can proudly run paid marketing from and know that your presence helps attract leads and lower your lead cost.</p>
      </div>
      <div class="channel">
        <h2 class="channel-title">Careerlink</h2>
        <p class="channel-text small">That uses all of the new features released in 2021, and you'll work with my team to apply tweaks to your profile so that you get found by more of your target prospects as they're searching for people like you.</p>
      </div>
      <div class="channel">
        <h2 class="channel-title">Own Website</h2>
        <p class="channel-text">That you can proudly run paid marketing from and know that your presence helps attract leads and lower your lead cost.</p>
      </div>
    </section>

    <div class="cta">GET STARTED NOW</div>
  </main>
</body>
</html>
```